RVKE website

The design should be based on the style and layout of the Talvi website (https://www.talvirex.ae/about-us) , incorporating softer tones.
Use RVKE green for headers and ash grey for other elements to maintain brand consistency.
The top of the homepage should include a dynamic counter that displays the number of projects we are currently working on and their total value.

Then going into Who we are, Vision, Mission, Directors, Our Values then Current Projects.
The current project wont link to any where right now but would like this option later on.

The bottom of the homepage should feature a section dedicated to showcasing the logos or names of our key clients.

This website will be an essential tool for communicating our expertise and engaging with potential clients, so it should be visually appealing, user-friendly, and aligned with our brand identity.

```html
<!DOCTYPE html>
<html lang="en">
<head>
<meta charset="utf-8">
<title>RVKE – Home</title>
<link rel="stylesheet" href="https://fonts.googleapis.com/css2?family=Krona+One&family=Roboto:wght@400;500;700&family=Lato:wght@400;700&display=swap">
<style>
:root{
  --green:#008a63;
  --ash:#4a4b4d;
  --ash-dark:#3c3d3f;
  --white:#ffffff;
  --text:#5a5a5a;
  --heading:#3a3a3a;
}
*{box-sizing:border-box;margin:0;padding:0}
html,body{width:1200px;height:2799px;overflow:hidden;background:var(--white);font-family:"Roboto",Arial,sans-serif}
.page{position:relative;width:1200px;height:2799px}
.abs{position:absolute}

.header{left:0;top:0;width:1200px;height:58px;background:var(--green)}
.brand{left:0;top:0;width:380px;height:58px;background:var(--white);display:flex;align-items:center;padding-left:112px;gap:10px}
.brand-mark{width:22px;height:22px;border-radius:50%;background:var(--green)}
.brand-name{font-family:"Krona One",sans-serif;font-size:30px;color:var(--green)}
.nav{left:414px;top:0;height:58px;display:flex;align-items:center;gap:23px;font-size:13px;font-weight:500;color:var(--white)}
.nav .active{text-decoration:underline}
.phone{left:960px;top:0;height:58px;display:flex;align-items:center;gap:9px;font-size:13px;font-weight:500;color:var(--white)}

.hero{left:0;top:58px;width:1200px;height:557px;background:linear-gradient(180deg,#3f8be0 0%,#6fb0ee 55%,#8cc3ee 75%,#4a7a4e 100%)}
.hero-city{left:640px;top:80px;width:560px;height:477px;background:linear-gradient(180deg,rgba(40,90,170,.35),rgba(25,60,120,.55) 70%,rgba(40,90,50,.7));border-radius:140px 140px 0 0}
.hero-title{left:109px;top:206px;font-family:"Krona One",sans-serif;font-size:43px;line-height:56px;color:var(--white)}
.btn{display:flex;align-items:center;justify-content:center;width:144px;height:46px;border-radius:23px;font-size:15px;font-weight:500}
.btn-light{left:111px;top:452px;background:var(--white);color:#222}
.dots{left:576px;top:542px;display:flex;gap:6px}
.dots span{width:13px;height:13px;border-radius:50%;background:var(--white)}
.dots .on{background:var(--green)}

.counter{top:615px;height:71px;display:flex;align-items:center;justify-content:center;font-family:"Krona One",sans-serif;font-size:21px;color:var(--white)}
.counter-projects{left:0;width:602px;background:var(--ash)}
.counter-value{left:602px;width:598px;background:var(--green)}
.fade{left:0;top:686px;width:1200px;height:60px;background:linear-gradient(#ececec,#fff)}

.feature-photo{left:112px;top:757px;width:976px;height:419px;background:linear-gradient(180deg,#1f5aa0 0%,#3a6fa5 45%,#2a2f3c 65%,#8a5a2a 85%,#c07a30 100%)}

.section-title{font-family:"Krona One",sans-serif;font-size:34px;color:var(--heading)}
.section-title em{font-style:normal;color:var(--green)}
.who-title{left:111px;top:1262px}
.who-text{left:111px;width:980px;font-size:14px;line-height:28.3px;color:var(--text)}
.p1{top:1322px}.p2{top:1418px}
.btn-dark{left:111px;top:1528px;background:var(--ash);color:var(--white)}

.values{left:0;top:1650px;width:1200px;height:678px;background:linear-gradient(135deg,#515255,#45464a 50%,#3e3f42)}
.values-title{left:111px;top:1705px;color:var(--white)}
.v-line{left:601px;top:1742px;width:5px;height:555px;background:var(--green)}
.h-line{top:2022px;height:5px;background:var(--green)}
.h-left{left:185px;width:305px}.h-right{left:707px;width:304px}
.integrity{left:490px;top:2008px;width:217px;text-align:center;font-family:"Krona One",sans-serif;font-size:27px;color:var(--white)}
.value-label{font-family:"Lato",sans-serif;font-size:31px;color:var(--white);transform:translate(-50%,-50%);white-space:nowrap}
.card{left:648px;top:1766px;width:363px;height:205px;background:var(--white);border-radius:5px;padding:26px 24px}
.card-head{display:flex;align-items:center;gap:32px}
.card-head h3{font-family:"Lato",sans-serif;font-weight:400;font-size:31px;color:var(--ash)}
.card p{margin-top:20px;font-family:"Lato",sans-serif;font-size:13px;line-height:28px;color:var(--text)}

.map{left:0;top:2328px;width:1200px;height:431px;background:linear-gradient(90deg,#e6e4dd 0%,#e6e4dd 30%,#86cbdc 38%,#86cbdc 55%,#e4e0d3 62%,#e8e6df 85%,#86cbdc 100%)}
.footer{left:0;top:2759px;width:1200px;height:40px;background:var(--ash-dark);display:flex;align-items:center;padding:0 117px;justify-content:space-between;font-size:14px;color:var(--white)}
.social{width:20px;height:20px;border-radius:3px;background:var(--white);margin-right:-40px}
</style>
</head>
<body>
<div class="page">
  <header class="abs header"></header>
  <div class="abs brand"><span class="brand-name">RVKE</span><span class="brand-mark"></span></div>
  <nav class="abs nav">
    <span class="active">Home</span><span>Who we are</span><span>Vision</span><span>Mission</span><span>Directors</span><span>Values</span><span>Contact Us</span>
  </nav>
  <div class="abs phone">
    <svg width="16" height="16" viewBox="0 0 24 24" fill="#fff"><path d="M6.6 10.8a15.1 15.1 0 0 0 6.6 6.6l2.2-2.2a1 1 0 0 1 1-.25 11.4 11.4 0 0 0 3.6.57 1 1 0 0 1 1 1V20a1 1 0 0 1-1 1A17 17 0 0 1 3 4a1 1 0 0 1 1-1h3.5a1 1 0 0 1 1 1c0 1.25.2 2.45.57 3.6a1 1 0 0 1-.25 1z"/></svg>
    <span>+1 555 010 2040</span>
  </div>

  <section class="abs hero" role="img" aria-label="City skyline with tall glass towers and palm trees under a blue sky"></section>
  <div class="abs hero-city" role="img" aria-label="Cluster of modern skyscrapers"></div>
  <h1 class="abs hero-title">Engineering<br>solutions for a more<br>productive &amp;<br>innovative future</h1>
  <a class="abs btn btn-light">Get Started</a>
  <div class="abs dots"><span></span><span class="on"></span><span></span></div>

  <div class="abs counter counter-projects">Number Of Projects : 300+</div>
  <div class="abs counter counter-value">Total Value : AED 25M</div>
  <div class="abs fade"></div>

  <div class="abs feature-photo" role="img" aria-label="Night view of a city with skyscrapers and lit highway interchanges"></div>

  <h2 class="abs section-title who-title">Who <em>We Are</em></h2>
  <p class="abs who-text p1">Sed ut perspiciatis unde omnis iste natus error sit voluptatem accusantium doloremque laudantium, totam rem aperiam, eaque ipsa quae ab illo inventore veritatis et quasi architecto beatae vitae dicta sunt explicabo. Nemo enim ipsam voluptatem quia voluptas sit aspernatur aut odit aut fugit, sed quia consequuntur magni dolores eos qui ratione voluptatem sequi nesciunt.</p>
  <p class="abs who-text p2">Neque porro quisquam est, qui dolorem ipsum quia dolor sit amet, consectetur, adipisci velit, sed quia non numquam eius modi tempora incidunt ut labore et dolore magnam aliquam quaerat voluptatem. Ut enim ad minima veniam, quis nostrum exercitationem ullam corporis suscipit laboriosam, nisi ut aliquid ex ea commodi consequatur? Quis autem vel eum iure reprehenderit qui in ea voluptate velit esse quam nihil</p>
  <a class="abs btn btn-dark">Read More</a>

  <section class="abs values"></section>
  <h2 class="abs section-title values-title">Our <em>Values</em></h2>
  <div class="abs v-line"></div>
  <div class="abs h-line h-left"></div>
  <div class="abs h-line h-right"></div>
  <div class="abs integrity">INTEGRITY</div>
  <div class="abs value-label" style="left:329px;top:1891px">Excellence</div>
  <div class="abs value-label" style="left:330px;top:2125px">Technology</div>
  <div class="abs value-label" style="left:773px;top:2135px">Collaboration</div>
  <div class="abs card">
    <div class="card-head">
      <svg width="56" height="56" viewBox="0 0 56 56" fill="none" stroke="#008a63" stroke-width="2.5">
        <circle cx="26" cy="26" r="12"/>
        <path d="M20 26l4 4 8-8"/>
        <path d="M8 32a19 19 0 0 1 26-23"/>
        <path d="M44 20a19 19 0 0 1-16 28"/>
        <path d="M30 6l5 3-3 5"/>
        <path d="M40 50h12M48 46l4 4-4 4"/>
      </svg>
      <h3>Agility</h3>
    </div>
    <p>Lorem ipsum dolor sit amet, consectetur adipiscing elit, sed do eiusmod tempor incididunt ut labore et dolore magna aliqua.</p>
  </div>

  <section class="abs map" role="img" aria-label="Regional map showing office locations across the Gulf"></section>

  <footer class="abs footer">
    <span>© 2024 RVKE. All rights reserved.</span>
    <span class="social"></span>
  </footer>
</div>
</body>
</html>
```